We have a blog www.lottamarie.eu based on WordPress (Wix would be also good) about homeopathy-critique and health issues.
Our logo is a little girl Hildegard, the background color green.
It looks somehow good, but we want to be up to date:).
Our goal is to open eyes from propaganda and misinformation on the web. We are all volunteers and invest our time and money for this purpose. Once people like it, we are happy to translate our blog to the English.
Updates

Please, don't submit a new design. we will choose from the designs we already have. Thank you! Added Thursday, July 20, 2017

Target Market(s)

mothers, people reading about health

Industry/Entity Type

Health

Number of Pages Required

3 page

Colors
abd037

Requirements
Must have
• - nice, friendly, evoking positive emotions
• - colorful (see for example how it looks now)
• - a good way how to show up articles (actually, if you open an article, you have to scroll, it appears on the bottom of the page)
• - We need to arrange stuff, where to put "most read", "Category", "contact", "themes" "search" (now, everything is on the right side. if you like it so, ok)
Nice to have
• Everything is in German, but I am happy to translate everything you need.
• The big text is: Lottchen mag kein Kraut: Hildegard wants no Kraut (the sugar pills of homeopathy)
• "(Nicht nur) homöopathiekritische Informationen für Eltern und alle, die für unsere Kleinen sorgen" - (Not only) Homeopathy-critique Information for Parents and All Who Take Care Of Our Small (Children)
• - there are many of the pictures of Hildegard, you can choose the best one. You can find them here https://www.verbund-klartext.eu/lottchen-mag-kein-kraut
• - we have also a FB, which could be integrated https://www.facebook.com/lottchenmagkeinkraut/?fref=ts
Should not have
• - a sterile modern look

```html
<!DOCTYPE html>
<html lang="de">
<head>
<meta charset="utf-8">
<title>Lottchen mag kein Kraut</title>
<link rel="stylesheet" href="https://fonts.googleapis.com/css2?family=Karla:wght@400;700&family=Varela+Round&display=swap">
<style>
  :root {
    --green: #8aae5a;
    --green-text: #8db35d;
    --red: #c1272d;
    --pink-bg: #f7e9ec;
    --mint-bg: #f1f5ec;
    --band-bg: #f3f6ee;
    --dark: #333333;
    --ink: #4a4a4a;
    --muted: #8a8a8a;
    --gold: #b9a23a;
  }
  * { box-sizing: border-box; margin: 0; padding: 0; }
  html, body { width: 1200px; height: 1172px; overflow: hidden; background: #fff; }
  body { position: relative; font-family: "Karla", sans-serif; color: var(--ink); }

  .masthead { position: absolute; left: 0; top: 0; width: 1200px; height: 229px; }
  .masthead-art {
    position: absolute; left: 340px; top: 22px; width: 462px; height: 207px; border-radius: 40% 40% 0 0;
    background: radial-gradient(ellipse at 50% 55%, #f6c9d2 0%, #f7e0e4 38%, #eef3e6 65%, rgba(255,255,255,0) 78%);
  }
  .brand {
    position: absolute; left: 400px; top: 150px; width: 400px; text-align: center;
    display: flex; align-items: center; justify-content: center; gap: 10px;
    font-family: "Karla", sans-serif; font-weight: 700; font-size: 22px; letter-spacing: 1px; color: var(--ink);
  }
  .brand i { width: 12px; height: 12px; border-radius: 50%; background: var(--green); display: inline-block; }

  .main-nav {
    position: absolute; left: 0; top: 229px; width: 1200px; height: 61px; background: var(--green);
    display: flex; align-items: center; justify-content: center; gap: 30px;
    font-family: "Karla", sans-serif; font-weight: 700; font-size: 16px; letter-spacing: 1px; color: #fff;
  }
  .main-nav .social { font-size: 13px; letter-spacing: .5px; display: flex; align-items: center; gap: 5px; }
  .main-nav .social i { width: 7px; height: 7px; background: #fff; border-radius: 50%; display: inline-block; }
  .main-nav svg { display: block; }

  .tagline {
    position: absolute; left: 0; top: 297px; width: 1200px; height: 33px; background: var(--band-bg);
    text-align: center; line-height: 33px; font-size: 15px; letter-spacing: .4px; color: #555;
  }

  .post-card { position: absolute; top: 357px; width: 403px; }
  .post-card.pink { left: 23px; height: 786px; background: var(--pink-bg); }
  .post-card.mint { left: 450px; height: 789px; background: var(--mint-bg); }
  .post-image { width: 100%; }
  .pink .post-image { height: 268px; background: linear-gradient(160deg, #8aa45a 0%, #6f7b43 30%, #c9789a 55%, #3d3a36 80%, #5c6a3a 100%); }
  .mint .post-image { height: 271px; background: linear-gradient(150deg, #f4f4ef 0%, #dfe6d2 35%, #c7a98a 55%, #f2f1ec 75%, #9fbf6e 100%); }
  .post-body { padding: 0 48px; }
  .post-meta { text-align: center; font-size: 13px; color: #555; margin-top: 33px; }
  .post-meta .comments { margin-left: 24px; }
  .post-meta svg { vertical-align: -2px; margin-right: 4px; }
  .post-title {
    font-family: "Varela Round", sans-serif; font-weight: 400; font-size: 24px; line-height: 25px;
    letter-spacing: 1.3px; margin-top: 12px;
  }
  .post-title span { display: block; text-align: justify; text-align-last: justify; white-space: nowrap; }
  .pink .post-title { color: var(--red); }
  .mint .post-title { color: var(--green-text); }
  .byline { text-align: center; font-size: 13px; margin-top: 10px; }
  .pink .byline { color: var(--red); }
  .pink .byline span { color: var(--muted); }
  .mint .byline { color: #555; }
  .mint .byline span { color: var(--gold); }
  .excerpt { font-size: 14px; line-height: 24.6px; letter-spacing: .25px; text-align: justify; margin-top: 28px; color: #555; }
  .read-more {
    display: block; width: 156px; height: 45px; margin: 43px auto 0; color: #fff;
    font-family: "Karla", sans-serif; font-weight: 700; font-size: 17px; letter-spacing: 1px;
    text-align: center; line-height: 45px;
  }
  .pink .read-more { background: var(--red); }
  .mint .read-more { background: var(--green); }
  .tags { font-size: 11px; line-height: 18px; margin-top: 38px; }
  .tags span { margin-right: 9px; }
  .pink .tags .cat { color: var(--muted); }
  .pink .tags .tag { color: var(--red); }
  .mint .tags span { color: var(--gold); }
  .mint .tags .tag { color: var(--green-text); }
  .corner-art { position: absolute; border-radius: 50%; }
  .pink .corner-art { right: 20px; bottom: 28px; width: 88px; height: 80px; background: radial-gradient(circle, #f6c3c3 0%, rgba(247,233,236,0) 70%); }
  .mint .corner-art { right: 24px; bottom: 24px; width: 80px; height: 100px; background: radial-gradient(ellipse, #cfe0b4 0%, rgba(241,245,236,0) 70%); }

  .sidebar { position: absolute; left: 877px; top: 357px; width: 298px; }
  .cat-row { height: 45px; margin-bottom: 11px; display: flex; }
  .cat-row .cat-name {
    flex: 1; color: #fff; font-family: "Karla", sans-serif; font-weight: 700; font-size: 16px; letter-spacing: 1.5px;
    line-height: 45px; padding-left: 26px;
  }
  .cat-row .count { width: 87px; background: var(--dark); color: #fff; font-size: 15px; line-height: 45px; text-align: center; }
  .bg-placebo { background: linear-gradient(90deg, #b0727f, #c8909c 60%, #b98590); }
  .bg-homoeo { background: linear-gradient(90deg, #777, #9a9a9a 55%, #e6e6e6 80%, #cfcfcf); }
  .bg-natur { background: linear-gradient(90deg, #3e7a2c, #5a9a3c 60%, #3f6f2d); }

  .widget-title {
    margin-top: 6px; height: 48px; background: var(--green); color: #fff; padding-left: 27px;
    font-family: "Karla", sans-serif; font-weight: 700; font-size: 17px; letter-spacing: 1.5px; line-height: 48px;
  }
  .popular { position: relative; height: 470px; overflow: hidden; }
  .pop-item { position: absolute; left: 0; width: 298px; height: 90px; }
  .pop-thumb { position: absolute; left: 0; top: 0; width: 71px; height: 71px; }
  .thumb-bee { background: linear-gradient(135deg, #7b6fc4, #9c8fd8 45%, #e7b52a 80%); }
  .thumb-baby { background: linear-gradient(135deg, #f0efed, #e6d8cf 60%, #d8c4b8); }
  .thumb-arnika { background: linear-gradient(135deg, #e0a21a, #f2c230 45%, #5f7f2c); }
  .pop-title { position: absolute; left: 98px; right: 0; top: -1px; font-size: 14px; line-height: 25.5px; letter-spacing: .8px; text-align: justify; color: #444; }
  .pop-date { position: absolute; left: 98px; top: 65px; font-size: 11.5px; color: var(--muted); }
</style>
</head>
<body>

<header class="masthead">
  <div class="masthead-art" role="img" aria-label="Aquarell-Blumenkranz mit Rosen und Beeren hinter dem Maskottchen"></div>
  <div class="brand"><i></i>Lottchen mag kein Kraut</div>
</header>

<nav class="main-nav">
  <span>Home / Beitragsseite</span>
  <span>Willkommen beim Lottchen!</span>
  <span>Lottchens Shop</span>
  <span class="social"><i></i>Hallonetz</span>
  <span class="social"><i></i>Piepser</span>
  <span class="social"><i></i>Filmkiste</span>
  <svg width="20" height="20" viewBox="0 0 20 20" aria-label="Suche"><circle cx="8" cy="8" r="6" fill="none" stroke="#c9dbb0" stroke-width="2.4"/><line x1="12.5" y1="12.5" x2="18" y2="18" stroke="#c9dbb0" stroke-width="2.6" stroke-linecap="round"/></svg>
</nav>

<div class="tagline">(Nicht nur) homöopathiekritische Informationen für Eltern und alle, die für unsere Kleinen sorgen</div>

<article class="post-card pink">
  <div class="post-image" role="img" aria-label="Kräuter, Blüten, Mörser und Fläschchen mit Tinkturen auf Holz"></div>
  <div class="post-body">
    <p class="post-meta">July 20th, 2017<span class="comments"><svg width="14" height="13" viewBox="0 0 14 13"><path d="M7 1C3.7 1 1 3.1 1 5.8c0 1.4.8 2.7 2 3.5L2.5 12l3-1.8c.5.1 1 .2 1.5.2 3.3 0 6-2.1 6-4.7S10.3 1 7 1z" fill="none" stroke="#e0556a" stroke-width="1.3"/></svg>5 comments</span></p>
    <h2 class="post-title"><span>Selbstmedikation mit</span><span>Homöopathie – klar! …</span><span>oder doch nicht so klar?</span></h2>
    <p class="byline">by <span>Author</span></p>
    <p class="excerpt">„Ham se da nich was Homöopatisches?“ Diese Frage hört man so manches Mal in Apotheken, oft sogar, wenn eigentlich ein schlichtes Rezept eingelöst werden soll und die falsche Angst vor der „bösen Chemie“ mal wieder zuschlägt.</p>
    <a class="read-more">Read More</a>
    <p class="tags"><span class="cat">Allgemein</span><span class="cat">Homöopathie</span><span class="cat">Placebo</span><span class="cat">Pseudomedizin</span><br><span class="tag">Globuli</span><span class="tag">Homöopathie</span><span class="tag">Placebo</span></p>
  </div>
  <div class="corner-art" role="img" aria-label="Zarte Aquarellblüte"></div>
</article>

<article class="post-card mint">
  <div class="post-image" role="img" aria-label="Weiße Kirschblüten und Holzlöffel mit Globuli"></div>
  <div class="post-body">
    <p class="post-meta">July 20th, 2017<span class="comments"><svg width="14" height="13" viewBox="0 0 14 13"><path d="M7 1C3.7 1 1 3.1 1 5.8c0 1.4.8 2.7 2 3.5L2.5 12l3-1.8c.5.1 1 .2 1.5.2 3.3 0 6-2.1 6-4.7S10.3 1 7 1z" fill="none" stroke="#8db35d" stroke-width="1.3"/></svg>5 comments</span></p>
    <h2 class="post-title"><span>Selbstmedikation mit</span><span>Homöopathie – klar! …</span><span>oder doch nicht so klar?</span></h2>
    <p class="byline">by <span>Author</span></p>
    <p class="excerpt">„Ham se da nich was Homöopatisches?“ Diese Frage hört man so manches Mal in Apotheken, oft sogar, wenn eigentlich ein schlichtes Rezept eingelöst werden soll und die falsche Angst vor der „bösen Chemie“ mal wieder zuschlägt.</p>
    <a class="read-more">Read More</a>
    <p class="tags"><span>Allgemein</span><span>Homöopathie</span><span>Placebo</span><span>Pseudomedizin</span><br><span class="tag">Globuli</span><span class="tag">Homöopathie</span><span class="tag">Placebo</span></p>
  </div>
  <div class="corner-art" role="img" aria-label="Aquarellzweig mit Blättern"></div>
</article>

<aside class="sidebar">
  <div class="cat-row"><span class="cat-name bg-placebo">Placebo</span><span class="count">3 posts</span></div>
  <div class="cat-row"><span class="cat-name bg-homoeo">Homöopathie</span><span class="count">6 posts</span></div>
  <div class="cat-row"><span class="cat-name bg-natur">Naturheilkunde</span><span class="count">2 posts</span></div>
  <div class="cat-row"><span class="cat-name bg-placebo">Placebo</span><span class="count">3 posts</span></div>
  <div class="cat-row"><span class="cat-name bg-homoeo">Homöopathie</span><span class="count">6 posts</span></div>

  <h3 class="widget-title">Popular Posts</h3>
  <div class="popular">
    <div class="pop-item" style="top:24px"><div class="pop-thumb thumb-bee" role="img" aria-label="Biene auf Asterblüte"></div><p class="pop-title">Apis mellifica – Was tut die Biene in den Globuli?</p><p class="pop-date">on July 22th, 2017</p></div>
    <div class="pop-item" style="top:127px"><div class="pop-thumb thumb-baby" role="img" aria-label="Kleinkind auf gepunkteter Decke"></div><p class="pop-title">Der Kinderdoc zur Reise-krankheit</p><p class="pop-date">on July 22th, 2017</p></div>
    <div class="pop-item" style="top:232px"><div class="pop-thumb thumb-arnika" role="img" aria-label="Gelbe Arnikablüten"></div><p class="pop-title">Arnika bei Bagatellver-letzungen</p><p class="pop-date">on July 22th, 2017</p></div>
    <div class="pop-item" style="top:337px"><div class="pop-thumb thumb-bee" role="img" aria-label="Biene auf Asterblüte"></div><p class="pop-title">Apis mellifica – Was tut die Biene in den Globuli?</p><p class="pop-date">on July 22th, 2017</p></div>
    <div class="pop-item" style="top:443px"><div class="pop-thumb thumb-arnika" role="img" aria-label="Gelbe Arnikablüten"></div><p class="pop-title">Arnika bei Bagatellver-letzungen</p></div>
  </div>
</aside>

</body>
</html>
```